Cardboard hanging box designs

I need to get some cardboard boxes made up for trailer wheel bearing kits. They need to be hanging boxes as pictured. The box needs to fit with our existing colour scheme and be clearly evident that it is for trailers. I am after 2 designs, one for "Trailer Bearing Kit" and one for "Marine Bearing Kit".
The Marine Bearing kit box should measure, 180mm High, 120mm Wide, 60mm Deep.
The Trailer Bearing kit box should measure, 180mm high, 120mm Wide, 30mm Deep.
These are all external measurements.

```html
<!DOCTYPE html>
<html lang="en">
<head>
<meta charset="utf-8">
<title>KRV Parts – Trailer Bearing Kit hanging box dieline</title>
<link rel="stylesheet" href="https://fonts.googleapis.com/css2?family=Montserrat:wght@500;600;800;900&display=swap">
<style>
  :root{
    --box-yellow:#f6e23c;
    --brand-red:#b8192c;
    --ink:#121212;
    --paper:#ffffff;
    --cut-line:#5a7fa8;
    --fold-line:#d2434f;
  }
  html,body{margin:0;padding:0;width:706px;height:1200px;overflow:hidden;background:var(--paper);}
  .dieline{display:block;width:706px;height:1200px;font-family:"Montserrat",sans-serif;}
  .panel-yellow{fill:var(--box-yellow);}
  .glue-flap{fill:var(--paper);stroke:var(--cut-line);stroke-width:1.2;}
  .hang-hole{fill:var(--box-yellow);stroke:var(--cut-line);stroke-width:1.4;}
  .fold{stroke:var(--fold-line);stroke-width:1;stroke-dasharray:3 3;fill:none;}
  .front-sky{fill:url(#skyGrad);}
  .swoosh{fill:var(--box-yellow);}
  .red-field{fill:var(--brand-red);}
  .product-photo{fill:url(#photoGrad);}
  .brand-name{font-family:"Montserrat",sans-serif;font-weight:900;fill:var(--ink);}
  .brand-sub{font-family:"Montserrat",sans-serif;font-weight:900;fill:var(--ink);letter-spacing:8px;}
  .fit-note{font-weight:600;font-size:11px;}
  .fit-note.on-red{fill:var(--box-yellow);}
  .fit-note.on-yellow{fill:var(--brand-red);}
  .kit-title{font-weight:900;}
  .kit-title.on-red{fill:var(--paper);font-size:27px;}
  .kit-title.on-yellow{fill:var(--ink);font-size:21px;}
  .rule-yellow{stroke:var(--box-yellow);stroke-width:1.6;}
  .rule-red{stroke:var(--brand-red);stroke-width:1.4;}
  .bearing-type{font-weight:500;font-size:11.5px;}
  .bearing-type.on-red{fill:var(--box-yellow);}
  .bearing-type.on-yellow{fill:var(--brand-red);font-size:11px;}
</style>
</head>
<body>
<svg class="dieline" viewBox="30 496 940 1598" xmlns="http://www.w3.org/2000/svg">
  <defs>
    <linearGradient id="skyGrad" x1="0" y1="0" x2="0" y2="1">
      <stop offset="0" stop-color="#ffffff"/>
      <stop offset="1" stop-color="#dcdce0"/>
    </linearGradient>
    <linearGradient id="photoGrad" x1="0" y1="0" x2="1" y2="1">
      <stop offset="0" stop-color="#8e9398"/>
      <stop offset="1" stop-color="#4a4e53"/>
    </linearGradient>
  </defs>

  <!-- glue flap -->
  <path class="glue-flap" d="M87,1120 L50,1126 L50,1544 L87,1550 Z"/>

  <!-- hanging header -->
  <g class="hang-header">
    <path class="panel-yellow" d="M90,1115 L90,990 Q90,980 100,980 L365,980 Q375,980 375,990 L375,1115 Z"/>
    <path class="hang-hole" d="M196,1014 L224,1014 Q232,1008 240,1014 L264,1014 Q272,1021 264,1028 L196,1028 Q188,1021 196,1014 Z"/>
    <path class="hang-hole" d="M196,1080 L224,1080 Q232,1070 240,1080 L264,1080 Q272,1088 264,1096 L196,1096 Q188,1088 196,1080 Z"/>
    <line class="fold" x1="90" y1="1055" x2="375" y2="1055"/>
  </g>

  <!-- side flaps top -->
  <path class="panel-yellow" d="M380,1115 L380,1042 L402,1020 L525,1020 L525,1115 Z"/>
  <path class="panel-yellow" d="M818,1115 L818,1020 L945,1020 L965,1042 L965,1115 Z"/>

  <!-- tuck lid -->
  <g class="tuck-lid">
    <path class="panel-yellow" d="M527,1115 L527,960 Q527,925 562,925 L783,925 Q818,925 818,960 L818,1115 Z"/>
    <line class="fold" x1="527" y1="985" x2="818" y2="985"/>
    <g transform="translate(675,1055) rotate(180)">
      <text class="brand-name" x="0" y="18" font-size="46" text-anchor="middle">KRV</text>
      <text class="brand-sub" x="4" y="36" font-size="14" text-anchor="middle">PARTS</text>
    </g>
  </g>

  <!-- bottom flaps -->
  <path class="panel-yellow" d="M87,1550 L378,1550 L378,1612 L320,1612 L320,1665 L148,1665 L148,1612 L87,1612 Z"/>
  <path class="panel-yellow" d="M378,1550 L525,1550 L525,1600 L490,1665 L413,1665 L378,1600 Z"/>
  <path class="panel-yellow" d="M525,1550 L818,1550 L818,1590 L760,1665 L585,1665 L525,1590 Z"/>
  <path class="panel-yellow" d="M818,1550 L965,1550 L965,1600 L930,1665 L853,1665 L818,1600 Z"/>

  <!-- front panel -->
  <g class="front-panel">
    <rect class="front-sky" x="87" y="1115" width="291" height="435"/>
    <path class="swoosh" d="M87,1240 C170,1300 290,1330 378,1295 L378,1550 L87,1550 Z"/>
    <path class="red-field" d="M87,1285 C180,1350 290,1395 378,1405 L378,1550 L87,1550 Z"/>
    <text class="brand-name" x="232" y="1210" font-size="60" text-anchor="middle">KRV</text>
    <text class="brand-sub" x="236" y="1238" font-size="18" text-anchor="middle">PARTS</text>
    <rect class="product-photo" x="100" y="1262" width="168" height="158" rx="16" role="img" aria-label="Photo of trailer bearing kit: two tapered roller bearings, oil seal and split pin"/>
    <text class="fit-note on-red" x="352" y="1421" text-anchor="end">Fits 1-1/16"</text>
    <text class="fit-note on-red" x="352" y="1435" text-anchor="end">Straight Spindle</text>
    <line class="rule-yellow" x1="145" y1="1444" x2="352" y2="1444"/>
    <text class="kit-title on-red" x="352" y="1476" text-anchor="end">TRAILER</text>
    <text class="kit-title on-red" x="352" y="1505" text-anchor="end">BEARING KIT</text>
    <line class="rule-yellow" x1="145" y1="1514" x2="352" y2="1514"/>
    <text class="bearing-type on-red" x="352" y="1530" text-anchor="end">TARROW TYPE BEARINGS</text>
  </g>

  <!-- side panel left -->
  <g class="side-panel">
    <rect class="panel-yellow" x="378" y="1115" width="147" height="435"/>
    <g transform="translate(452,1245) rotate(-90)">
      <text class="brand-name" x="0" y="10" font-size="52" text-anchor="middle">KRV</text>
      <text class="brand-sub" x="4" y="28" font-size="14" text-anchor="middle">PARTS</text>
    </g>
    <text class="fit-note on-yellow" x="452" y="1381" text-anchor="middle">Fits 1-1/16"</text>
    <text class="fit-note on-yellow" x="452" y="1395" text-anchor="middle">Straight Spindle</text>
    <line class="rule-red" x1="398" y1="1404" x2="506" y2="1404"/>
    <text class="kit-title on-yellow" x="452" y="1432" text-anchor="middle">TRAILER</text>
    <text class="kit-title on-yellow" x="452" y="1456" text-anchor="middle">BEARING</text>
    <text class="kit-title on-yellow" x="452" y="1480" text-anchor="middle">KIT</text>
    <line class="rule-red" x1="398" y1="1490" x2="506" y2="1490"/>
    <text class="bearing-type on-yellow" x="452" y="1508" text-anchor="middle">TARROW TYPE</text>
    <text class="bearing-type on-yellow" x="452" y="1521" text-anchor="middle">BEARINGS</text>
  </g>

  <!-- back panel -->
  <g class="back-panel">
    <rect class="front-sky" x="525" y="1115" width="293" height="435"/>
    <path class="swoosh" d="M525,1215 C610,1280 730,1320 818,1290 L818,1550 L525,1550 Z"/>
    <path class="red-field" d="M525,1255 C620,1330 730,1395 818,1405 L818,1550 L525,1550 Z"/>
    <text class="brand-name" x="675" y="1220" font-size="60" text-anchor="middle">KRV</text>
    <text class="brand-sub" x="679" y="1248" font-size="18" text-anchor="middle">PARTS</text>
    <rect class="product-photo" x="638" y="1262" width="168" height="158" rx="16" role="img" aria-label="Photo of trailer bearing kit: two tapered roller bearings, oil seal and split pin"/>
    <text class="fit-note on-red" x="542" y="1421">Fits 1-1/16"</text>
    <text class="fit-note on-red" x="542" y="1435">Straight Spindle</text>
    <line class="rule-yellow" x1="542" y1="1444" x2="748" y2="1444"/>
    <text class="kit-title on-red" x="542" y="1476">TRAILER</text>
    <text class="kit-title on-red" x="542" y="1505">BEARING KIT</text>
    <line class="rule-yellow" x1="542" y1="1514" x2="748" y2="1514"/>
    <text class="bearing-type on-red" x="542" y="1530">TARROW TYPE BEARINGS</text>
  </g>

  <!-- side panel right -->
  <g class="side-panel">
    <rect class="panel-yellow" x="818" y="1115" width="147" height="435"/>
    <g transform="translate(892,1245) rotate(-90)">
      <text class="brand-name" x="0" y="10" font-size="52" text-anchor="middle">KRV</text>
      <text class="brand-sub" x="4" y="28" font-size="14" text-anchor="middle">PARTS</text>
    </g>
    <text class="fit-note on-yellow" x="892" y="1381" text-anchor="middle">Fits 1-1/16"</text>
    <text class="fit-note on-yellow" x="892" y="1395" text-anchor="middle">Straight Spindle</text>
    <line class="rule-red" x1="838" y1="1404" x2="946" y2="1404"/>
    <text class="kit-title on-yellow" x="892" y="1432" text-anchor="middle">TRAILER</text>
    <text class="kit-title on-yellow" x="892" y="1456" text-anchor="middle">BEARING</text>
    <text class="kit-title on-yellow" x="892" y="1480" text-anchor="middle">KIT</text>
    <line class="rule-red" x1="838" y1="1490" x2="946" y2="1490"/>
    <text class="bearing-type on-yellow" x="892" y="1508" text-anchor="middle">TARROW TYPE</text>
    <text class="bearing-type on-yellow" x="892" y="1521" text-anchor="middle">BEARINGS</text>
  </g>
</svg>
</body>
</html>
```